Healthcare technology company needs website design

We need a logo for a new company based in the U.S. We develop software to assist consumers identifying lowest cost healthcare coverage methods, including insurance, discount cards, and cash options. We would like to see designs that use multiple shades of green with the optional addition of other complimentary colors. The final design should communicate a unique blend of saving money while receiving the healthcare you need.
Need the following pages/sections: Homepage, Solutions, About Us, Contact
Competitors: www.velorinhealth.example; www.qdplm.example

Target Market(s)

Businesses

Industry/Entity Type

Healthcare

Coding

Coded - Design and coding required

Number of Pages Required

4 page

Colors
0054AA
0677BA
7BADD7
CADEEF
E8F1F8
00AB8E
00BBA5
67D7C9
C6EFE9
E9F9F6

Requirements
Must have
• Matching color theme with logo
Nice to have
• Animated background

```html
<!DOCTYPE html>
<html lang="en">
<head>
<meta charset="utf-8">
<title>Fernvale Health — Healthcare Technology Company</title>
<link href="https://fonts.googleapis.com/css2?family=Poppins:wght@400;500;600;700&display=swap" rel="stylesheet">
<style>
:root{
  --green:#1fa84a;
  --blue:#0677BA;
  --blue-deep:#0054AA;
  --teal:#00AB8E;
  --mint:#E9F9F6;
  --mint-2:#e6f4ea;
  --sky:#CADEEF;
  --ink:#222b33;
  --muted:#555d66;
  --line:#d9e6ef;
  --white:#ffffff;
  --grad:linear-gradient(90deg,#22b14c 0%,#0a82cc 100%);
}
*{box-sizing:border-box;margin:0;padding:0}
html,body{width:1200px;height:3431px;overflow:hidden}
body{position:relative;font-family:"Poppins",sans-serif;color:var(--ink);background:var(--white)}
.abs{position:absolute}
a{color:inherit;text-decoration:none}

/* header / hero */
.hero-shape{left:600px;top:0;width:600px;height:712px;background:linear-gradient(180deg,#1aa751 0%,#0e8fb8 60%,#0a82cc 100%);border-bottom-left-radius:300px}
.brand{display:flex;align-items:center;gap:8px;font-weight:700;font-size:17px;letter-spacing:1px;color:var(--green);white-space:nowrap}
.brand-dot{width:22px;height:22px;border-radius:50%;background:var(--green)}
.header-brand{left:60px;top:40px}
.nav{left:665px;top:30px;display:flex;gap:24px;font-size:13px;color:var(--white)}
.nav a.active{position:relative}
.nav a.active::after{content:"";position:absolute;left:50%;top:22px;margin-left:-4px;border:4px solid transparent;border-top-color:#fff}
.phone-btn{left:975px;top:20px;width:164px;height:40px;border-radius:8px;background:#1fa84a;color:#fff;display:flex;align-items:center;justify-content:center;gap:10px;font-size:15px;font-weight:500;white-space:nowrap}
.eyebrow{left:60px;top:212px;font-size:17px;color:var(--green)}
.hero-title{left:58px;top:248px;font-size:46px;line-height:53px;font-weight:700;color:var(--blue);white-space:nowrap}
.hero-text{left:61px;top:364px;width:425px;font-size:13px;line-height:21px;color:var(--ink)}
.btn{display:flex;align-items:center;justify-content:center;border-radius:8px;color:#fff;font-size:15px;font-weight:500;letter-spacing:.3px;background:var(--grad)}
.hero-btn{left:60px;top:442px;width:142px;height:40px}
.pager{left:60px;top:585px;display:flex;align-items:flex-end;gap:8px;font-size:14px;font-weight:600}
.pager-line{width:66px;height:1px;background:var(--blue);margin-bottom:6px}
.pager .cur{color:var(--green);margin-bottom:8px}
.hero-art{left:705px;top:150px;width:435px;height:430px;border-radius:40px;background:linear-gradient(160deg,rgba(255,255,255,.35),rgba(60,200,110,.45))}

/* section headings */
.sec-title{font-size:34px;font-weight:700;color:var(--green);letter-spacing:.5px;white-space:nowrap}
.rule{width:78px;height:2px;background:var(--green)}
.rule::after{content:"";display:block;margin:0 auto;width:26px;height:3px;background:var(--blue);transform:translateY(-0.5px)}
.sec-sub{font-size:13px;line-height:21px;color:var(--muted)}

/* solutions */
.sol-title{left:0;width:1200px;top:758px;text-align:center}
.sol-rule{left:561px;top:814px}
.sol-sub{left:0;width:1200px;top:832px;text-align:center}
.sol-card{top:903px;width:271px;height:305px;background:#fff;border-radius:8px;box-shadow:0 4px 18px rgba(20,60,90,.10);border-bottom:4px solid #2a9d9a;text-align:center}
.sol-card .art{margin:16px auto 0;width:120px;height:113px;border-radius:10px;background:linear-gradient(135deg,var(--mint-2),#c9ead3)}
.sol-card h3{margin-top:22px;font-size:21px;font-weight:600;color:var(--green)}
.sol-card p{margin:12px auto 0;width:220px;font-size:12px;line-height:20px;color:var(--muted)}
.sol-card a{display:inline-block;margin-top:18px;font-size:13px;color:var(--blue);text-decoration:underline}

/* about */
.about-band{left:0;top:1304px;width:1200px;height:413px;background:var(--grad)}
.about-arch{left:189px;top:1357px;width:336px;height:360px;background:#fff;border-radius:168px 168px 0 0}
.about-art{left:214px;top:1420px;width:286px;height:297px;border-radius:143px 143px 0 0;background:linear-gradient(160deg,#e8f6ec,#bfe6c9)}
.about-eyebrow{left:615px;top:1370px;font-size:15px;color:#fff}
.about-title{left:613px;top:1392px;font-size:34px;font-weight:700;color:#fff;letter-spacing:.5px;white-space:nowrap}
.about-rule{left:615px;top:1444px;background:rgba(255,255,255,.6)}
.about-text{left:615px;top:1466px;width:400px;font-size:12px;line-height:21px;color:#fff}
.about-text p+p{margin-top:8px}
.about-btn{left:615px;top:1616px;width:142px;height:41px;border:1.5px solid #fff;background:#22b14c}

/* why choose */
.why-title{left:61px;top:1794px}
.why-rule{left:61px;top:1849px}
.why-sub{left:61px;top:1872px;width:390px}
.feat{width:246px;height:75px;border:1.5px solid var(--line);border-radius:10px;display:flex;align-items:center;gap:16px;padding-left:16px;font-size:15px;line-height:21px;color:var(--ink)}
.feat.on{background:var(--mint-2);border-color:var(--mint-2)}
.feat svg{width:44px;height:44px;flex:none;stroke:var(--green);fill:none;stroke-width:1.6}
.why-art{left:689px;top:1825px;width:430px;height:426px;border-radius:215px 215px 0 0;background:linear-gradient(180deg,#cfe4f5,#e4f0fa)}

/* impact */
.impact-band{left:0;top:2317px;width:1200px;height:307px;background:linear-gradient(120deg,#2f8fd8,#1f7fcf)}
.impact-title{left:0;width:1200px;top:2384px;text-align:center;font-size:29px;line-height:40px;font-weight:700;color:#fff;letter-spacing:.5px}
.impact-rule{left:561px;top:2479px;background:rgba(255,255,255,.6)}
.stat{top:2530px;width:188px;height:188px;border-radius:50%;background:#fff;box-shadow:0 6px 20px rgba(20,60,90,.10);text-align:center}
.stat b{display:block;margin-top:42px;font-size:45px;line-height:50px;font-weight:700;color:var(--green)}
.stat span{display:block;margin-top:8px;font-size:14px;line-height:19px;color:var(--ink)}

/* get started */
.gs-art{left:186px;top:2824px;width:389px;height:266px;border-radius:14px;background:linear-gradient(135deg,#eef4f9,#d6e6f3)}
.gs-title{left:632px;top:2810px}
.gs-rule{left:633px;top:2861px}
.gs-sub{left:633px;top:2884px;font-size:22px;line-height:30px;font-weight:500;color:var(--blue)}
.gs-input{left:633px;top:2963px;width:405px;height:40px;border:1.5px solid var(--line);border-radius:8px;padding-left:16px;display:flex;align-items:center;font-size:12px;color:var(--muted)}
.gs-btn{left:633px;top:3017px;width:143px;height:40px}

/* footer */
.footer{left:0;top:3165px;width:1200px;height:266px;background:linear-gradient(90deg,#22b14c 0%,#14a37a 45%,#0b8fb0 100%);border-top-left-radius:100px;color:#fff}
.footer .brand{color:#fff;font-size:24px}
.footer .brand-dot{background:#fff;width:30px;height:30px}
.f-brand{left:63px;top:56px}
.f-contact{left:80px;top:122px;font-size:13px;line-height:30px}
.f-contact div{display:flex;align-items:center;gap:16px;white-space:nowrap}
.f-contact svg{width:18px;height:18px;stroke:#fff;fill:none;stroke-width:1.5}
.f-col{top:52px;font-size:13px}
.f-col h4{font-size:14px;font-weight:600;letter-spacing:.5px;margin-bottom:12px}
.f-col ul{list-style:none;padding-left:18px}
.f-col li{line-height:24px;position:relative}
.f-col li::before{content:"";position:absolute;left:-17px;top:10px;width:4px;height:4px;border-radius:50%;background:#fff}
.socials{display:flex;gap:8px;margin-top:14px}
.socials span{width:36px;height:36px;border-radius:50%;border:1.5px solid #fff}
.f-rule{left:60px;top:221px;width:1080px;height:1px;background:rgba(255,255,255,.35)}
.copy{left:0;width:1200px;top:236px;text-align:center;font-size:12px}
</style>
</head>
<body>

<!-- Hero -->
<div class="abs hero-shape"></div>
<div class="abs brand header-brand"><span class="brand-dot"></span>FERNVALE HEALTH</div>
<nav class="abs nav">
  <a class="active" href="#">Home</a><a href="#">Solutions</a><a href="#">About Us</a><a href="#">Contact Us</a>
</nav>
<a class="abs phone-btn" href="#">
  <svg width="18" height="18" viewBox="0 0 24 24" fill="none" stroke="#fff" stroke-width="1.8"><path d="M5 3h4l2 5-2.5 1.5a11 11 0 0 0 6 6L16 13l5 2v4a2 2 0 0 1-2 2A17 17 0 0 1 3 5a2 2 0 0 1 2-2z"/></svg>
  555 010 2468
</a>
<div class="abs eyebrow">Healthcare Technology Company</div>
<h1 class="abs hero-title">Save Money + Lowest<br>Cost Healthcare</h1>
<p class="abs hero-text">We Develop Software To Assist Consumers Identifying Lowest Cost Healthcare Coverage Methods, Including Insurance, Discount Cards, And Cash Options</p>
<a class="abs btn hero-btn" href="#">CONTACT US</a>
<div class="abs pager"><span class="pager-line"></span><span class="cur">01</span><span>/03</span></div>
<div class="abs hero-art" role="img" aria-label="Illustration of a person on a beanbag with a laptop beside a savings dashboard showing discount card and insurance figures"></div>

<!-- Solutions -->
<h2 class="abs sec-title sol-title">OUR SOLUTIONS</h2>
<div class="abs rule sol-rule"></div>
<p class="abs sec-sub sol-sub">We Develop Software To Assist Consumers Identifying Lowest Cost<br>Healthcare Coverage Methods</p>

<div class="abs sol-card" style="left:142px">
  <div class="art" role="img" aria-label="Illustration of a tablet insurance form with a doctor"></div>
  <h3>Insurance</h3>
  <p>Lorem Ipsum has been the industry's standard dummy text ever since the when an unknown printer</p>
  <a href="#">Learn More</a>
</div>
<div class="abs sol-card" style="left:465px">
  <div class="art" role="img" aria-label="Illustration of a person holding a healthcare discount card"></div>
  <h3>Discount Cards</h3>
  <p>Lorem Ipsum has been the industry's standard dummy text ever since the when an unknown printer</p>
  <a href="#">Learn More</a>
</div>
<div class="abs sol-card" style="left:787px">
  <div class="art" role="img" aria-label="Illustration of a wallet with cash and coins"></div>
  <h3>Cash Options</h3>
  <p>Lorem Ipsum has been the industry's standard dummy text ever since the when an unknown printer</p>
  <a href="#">Learn More</a>
</div>

<!-- About -->
<div class="abs about-band"></div>
<div class="abs about-arch"></div>
<div class="abs about-art" role="img" aria-label="Illustration of a doctor with a clipboard stepping out of a phone next to an insurance form"></div>
<div class="abs about-eyebrow">About Us</div>
<h2 class="abs about-title">FERNVALE HEALTH</h2>
<div class="abs rule about-rule"></div>
<div class="abs about-text">
  <p>Lorem Ipsum is simply dummy text of the printing and typesetting industry. Lorem Ipsum has been the industry's standard.</p>
  <p>Lorem Ipsum is simply dummy text of the printing and typesetting industry. Lorem Ipsum has been the industry's standard dummy text ever since the 1500s, when an unknown printer took a galley of type and scrambled it to make a type specimen book.</p>
</div>
<a class="abs btn about-btn" href="#">LEARN MORE</a>

<!-- Why choose -->
<h2 class="abs sec-title why-title">WHY CHOOSE US</h2>
<div class="abs rule why-rule"></div>
<p class="abs sec-sub why-sub">We Develop Software To Assist Consumers Identifying Lowest Cost Healthcare Coverage Methods</p>

<div class="abs feat on" style="left:60px;top:1950px">
  <svg viewBox="0 0 44 44"><rect x="6" y="14" width="30" height="18" rx="2"/><rect x="10" y="10" width="30" height="18" rx="2"/><circle cx="25" cy="19" r="5"/></svg>
  <span>Revenue<br>Management</span>
</div>
<div class="abs feat" style="left:330px;top:1950px">
  <svg viewBox="0 0 44 44"><rect x="7" y="26" width="5" height="12"/><rect x="16" y="20" width="5" height="18"/><rect x="25" y="24" width="5" height="14"/><rect x="34" y="14" width="5" height="24"/><path d="M8 20l9-8 9 5 10-10"/></svg>
  <span>Smart<br>Analytics</span>
</div>
<div class="abs feat" style="left:60px;top:2047px">
  <svg viewBox="0 0 44 44"><rect x="6" y="6" width="24" height="32" rx="2"/><path d="M11 13h14M11 19h14M11 25h8"/><circle cx="33" cy="30" r="6"/><path d="M33 27v3l2 2"/></svg>
  <span>Reminders And<br>Alerts</span>
</div>
<div class="abs feat" style="left:330px;top:2047px">
  <svg viewBox="0 0 44 44"><rect x="10" y="5" width="24" height="34" rx="2"/><path d="M15 12h14M15 18h6M25 18h4M15 24h6M25 24h4M15 30h14"/></svg>
  <span>Automated<br>Billing</span>
</div>
<div class="abs feat" style="left:60px;top:2144px">
  <svg viewBox="0 0 44 44"><circle cx="22" cy="12" r="5"/><circle cx="11" cy="22" r="4"/><circle cx="33" cy="22" r="4"/><path d="M13 36c0-6 4-10 9-10s9 4 9 10M4 36c0-5 3-8 7-8M40 36c0-5-3-8-7-8"/></svg>
  <span>Patient<br>Portal</span>
</div>
<div class="abs feat" style="left:330px;top:2144px">
  <svg viewBox="0 0 44 44"><path d="M22 16c-3-6-12-5-12 2 0 6 12 12 12 12s12-6 12-12c0-7-9-8-12-2z"/><path d="M4 26l8 10h10M40 26l-8 10H22"/></svg>
  <span>Patient Health<br>Insurance</span>
</div>
<div class="abs why-art" role="img" aria-label="Illustration of a doctor waving from a laptop screen with insurance, billing and discount card tabs"></div>

<!-- Impact -->
<div class="abs impact-band" role="img" aria-label="Blue toned background photo of a medical consultation"></div>
<h2 class="abs impact-title">PROVEN IMPACT ON OUR HEALTH<br>INSURANCE CUSTOMERS</h2>
<div class="abs rule impact-rule"></div>
<div class="abs stat" style="left:280px"><b>28%</b><span>Uplift inCustomer<br>Engagement</span></div>
<div class="abs stat" style="left:506px"><b>64%</b><span>Improv in Sales<br>Conversion Rate</span></div>
<div class="abs stat" style="left:732px"><b>90%</b><span>Uplift inIntelligence<br>&amp; Automation</span></div>

<!-- Get started -->
<div class="abs gs-art" role="img" aria-label="Tablet, laptop and phone showing the healthcare platform dashboard"></div>
<h2 class="abs sec-title gs-title">GET STRATED WITH</h2>
<div class="abs rule gs-rule"></div>
<p class="abs gs-sub">Modern Technology Platform For<br>Healthcare Insurance</p>
<div class="abs gs-input">Enter Email *</div>
<a class="abs btn gs-btn" href="#">GET STARTED</a>

<!-- Footer -->
<footer class="abs footer">
  <div class="abs brand f-brand"><span class="brand-dot"></span>FERNVALE HEALTH</div>
  <div class="abs f-contact">
    <div><svg viewBox="0 0 24 24"><rect x="6" y="2" width="12" height="20" rx="2"/><path d="M11 18h2"/></svg>Call Us: 555.010.2468</div>
    <div><svg viewBox="0 0 24 24"><rect x="3" y="5" width="18" height="14" rx="1"/><path d="M3 6l9 7 9-7"/></svg>info@fernvalehealth.example</div>
  </div>
  <div class="abs f-col" style="left:360px">
    <h4>SITEMAP</h4>
    <ul><li>Home</li><li>Solutions</li><li>About Us</li><li>Contact Us</li></ul>
  </div>
  <div class="abs f-col" style="left:613px">
    <h4>SOLUTIONS</h4>
    <ul><li>Insurance</li><li>Discount Cards</li><li>Cash Options.</li></ul>
  </div>
  <div class="abs f-col" style="left:887px">
    <h4>FOLLOW US</h4>
    <div class="socials"><span></span><span></span><span></span></div>
  </div>
  <div class="abs f-rule"></div>
  <div class="abs copy">©FERNVALE HEALTH - 2022 All rights reserved.</div>
</footer>

</body>
</html>
```